Heron valley RV Resort business card

I need a design card for the logo I just had made on here. I will provide it and please make some cool designs, thank you.

I would like the card to have
- phone number (865-318-2967)
- email ( heronvalleyrv@pinemail.com)
- address to the park ( 5186 Quarry Gate Loop rd, Maryville, TN) ZIP: 37429
on the back for double sided id like some lines for writing on. thanks

please follow the logo we provided in the files, I can provide the photoshop file if you need it.

please note this is in the Smokey mountains of Tennessee

Target Market(s)

cabin/rv rentals

Industry/Entity Type

rv/campground/cabin rentals

Contact Information for Business Card

address/email/phone number I added details in brief

Requirements
Must have
• on the back add a bear or something cool

```html
<!DOCTYPE html>
<html lang="en">
<head>
<meta charset="utf-8">
<title>Heron valley RV Resort business card</title>
<link href="https://fonts.googleapis.com/css2?family=EB+Garamond:wght@400;500&display=swap" rel="stylesheet">
<style>
  :root {
    --backdrop: #c9c9c9;
    --card: #ffffff;
    --gold: #ae8a3c;
    --gold-soft: #d8c193;
  }
  html, body {
    margin: 0;
    padding: 0;
    overflow: hidden;
  }
  .canvas {
    position: relative;
    width: 1200px;
    height: 846px;
    background: var(--backdrop);
    font-family: "EB Garamond", Georgia, serif;
    color: var(--gold);
  }
  .card {
    position: absolute;
    top: 169px;
    width: 290px;
    height: 508px;
    background: var(--card);
  }
  .card--front { left: 280px; }
  .card--back { left: 634px; }
  .card__frame {
    position: absolute;
    inset: 15px 16px 15px 16px;
    border: 1px solid var(--gold);
    border-radius: 21px;
  }
  .brand {
    position: absolute;
    top: 118px;
    left: 0;
    width: 100%;
    text-align: center;
  }
  .brand__mark {
    display: block;
    margin: 0 auto 14px;
  }
  .brand__name {
    margin: 0;
    font-size: 27px;
    font-weight: 500;
    line-height: 1.15;
    color: var(--gold);
  }
  .contact {
    position: absolute;
    top: 322px;
    left: 0;
    width: 100%;
    text-align: center;
    font-weight: 400;
  }
  .contact__phone {
    margin: 0;
    font-size: 27px;
    line-height: 1;
  }
  .contact__email {
    margin: 8px 0 0;
    font-size: 16.5px;
  }
  .contact__address {
    margin: 22px 0 0;
    font-size: 16.5px;
    line-height: 1.25;
    font-style: normal;
  }
  .emblem {
    position: absolute;
    top: 120px;
    left: 69px;
    width: 152px;
    height: 152px;
    border-radius: 50%;
    border: 1.5px solid var(--gold);
    box-sizing: border-box;
    background: radial-gradient(circle at 50% 45%, #fbf5e8 0%, #f1e4c6 100%);
  }
  .notes {
    position: absolute;
    top: 313px;
    left: 47px;
    width: 200px;
    margin: 0;
    padding: 0;
    list-style: none;
  }
  .notes__line {
    height: 36px;
    border-top: 1px solid var(--gold-soft);
  }
</style>
</head>
<body>
  <main class="canvas">
    <section class="card card--front">
      <div class="card__frame"></div>
      <div class="brand">
        <svg class="brand__mark" width="40" height="40" viewBox="0 0 40 40" aria-hidden="true">
          <circle cx="20" cy="20" r="18" fill="none" stroke="var(--gold)" stroke-width="1.5"/>
        </svg>
        <p class="brand__name">Heron valley<br>RV Resort</p>
      </div>
      <div class="contact">
        <p class="contact__phone">Tel. 865-318-2967</p>
        <p class="contact__email">heronvalleyrv@pinemail.com</p>
        <address class="contact__address">5186 Quarry Gate Loop rd,<br>Maryville, TN 37429</address>
      </div>
    </section>

    <section class="card card--back">
      <div class="card__frame"></div>
      <div class="emblem" role="img" aria-label="Gold line-art emblem of a log cabin among pine trees beneath mountains and a rising sun"></div>
      <ul class="notes">
        <li class="notes__line"></li>
        <li class="notes__line"></li>
        <li class="notes__line"></li>
        <li class="notes__line"></li>
        <li class="notes__line"></li>
      </ul>
    </section>
  </main>
</body>
</html>
```